ReadNest Learning App for Children with Dyslexia

Project Description:

We are seeking a talented UI/UX designer to create engaging and intuitive designs for Readnest, an innovative educational app designed to help children learn letters and words through a multisensory learning approach. The app aims to be particularly helpful for children with dyslexia, providing a supportive and interactive learning environment.

Key App Features & Design Requirements:

Account Creation Screen: Design a welcoming and straightforward sign-up page that allows users to register with their email or continue with Quorvix. The design should be clean, focusing on user-friendliness and accessibility, adhering to our terms of service and privacy policy.

Main Screen Design: The main screen should allocate at least 4/6 of its height to the interactive drawing area. It needs to display word prompts in both correct and scrambled orders and include options to "Show all Words," "Play all words," and a search function. The interface should be vibrant, engaging, and easy to navigate for children.

Profile Section: Create a user-friendly profile page that allows users to edit their profile image, name, username, email, links, and bio. The design should be clean and encourage user engagement.

NestStats Page: This section will display the user's learning progress, including rankings, a learning curve, and recently learned words. It should visually represent progress in a motivating and understandable way, suitable for a younger audience.

Visual and Auditory Feedback Implementation: Incorporate elements that support visual and auditory feedback, using dyslexia-friendly formats. This includes choosing appropriate colors, fonts, and auditory cues.

Accessibility and Customization Settings: Designs should include settings for adjusting visual contrast, font size, and the word list to accommodate individual preferences and needs.

Feel free to add more interactions and/or pages.

Design preferences:

Color Scheme: Use a bright, inviting color palette that stimulates learning and engagement without overwhelming the users.
Font Selection: Opt for fonts that are readable and accessible, particularly for users with dyslexia.
Icons and Graphics: Design custom icons and graphics that are cohesive with the app's theme and purpose. Illustrations should be simple, relatable, and supportive of the learning process.

Target Market(s)

Educational

Industry/Entity Type

Educational

Colors
0054AA
0677BA
7BADD7
CADEEF
E8F1F8
0094D4
00A9DD
6FCCEA
C7EBF8
E9F6FB

Requirements
Must have
• Educational app, a writing area, scoring and account management
Nice to have
• Statistics, Ranking Page, Settings and some nice visual features

```html
<!DOCTYPE html>
<html lang="en">
<head>
<meta charset="utf-8">
<title>ReadNest Learning App</title>
<link href="https://fonts.googleapis.com/css2?family=Fredoka:wght@400;500;600&family=Nunito:wght@400;600;700;800&display=swap" rel="stylesheet">
<style>
:root{
  --board:#dce9f3;
  --ink:#1f1f24;
  --label:#9aa3ab;
  --navy:#0a46b3;
  --blue:#0054aa;
  --sky:#0fa0dd;
  --yellow:#f9cf25;
  --white:#ffffff;
  --line:#e4e4ea;
  --muted:#9a9aa6;
  --cream:#fdf3ef;
  --peach:#fde6cf;
  --grass:#5cbf3a;
}
*{box-sizing:border-box;margin:0;padding:0}
html,body{width:957px;height:1200px;overflow:hidden;background:var(--board)}
body{font-family:"Nunito",sans-serif;color:var(--ink)}
.board{position:absolute;left:0;top:0;width:1719px;height:2156px;transform:scale(0.5567);transform-origin:0 0}
.abs{position:absolute}
.board-title{position:absolute;left:0;width:100%;text-align:center;font-family:"Fredoka",sans-serif;font-weight:600;color:var(--ink)}
.section-label{position:absolute;font-family:"Fredoka",sans-serif;font-weight:500;font-size:34px;color:var(--label)}
.screen{position:absolute;width:284px;overflow:hidden;border-radius:22px;background:var(--cream)}
.app-header{position:absolute;left:0;top:0;width:100%;height:56px;background:var(--navy);color:var(--white)}
.app-header svg{position:absolute;left:0;top:52px}
.header-title{position:absolute;top:19px;font-family:"Fredoka",sans-serif;font-weight:500;font-size:13px}
.menu-dot{position:absolute;top:16px;width:24px;height:24px;border-radius:50%;background:var(--yellow)}
.menu-dot i{position:absolute;left:7px;width:10px;height:1.5px;background:#b88a00}
.points{position:absolute;right:10px;top:15px;height:24px;padding:0 8px 0 28px;border-radius:6px;background:var(--white);color:var(--navy);font-size:10px;font-weight:700;line-height:24px}
.points::before{content:"";position:absolute;left:9px;top:6px;width:9px;height:9px;border:2px solid var(--navy);border-radius:50%}
.play-body{position:absolute;left:0;top:56px;width:100%;bottom:0;background:linear-gradient(180deg,#fde9d6 0%,#fdf6e3 45%,#fce8ee 100%)}
.sound-btn{position:absolute;width:34px;height:32px;border-radius:7px;background:#eef0f6;box-shadow:0 2px 0 #d6d9e2}
.sound-btn svg{position:absolute;left:10px;top:9px}
.art{position:absolute;border-radius:40%;background:radial-gradient(circle at 50% 40%,#e5a35c,#9c5b2a 70%,transparent 71%)}
.answer-box{position:absolute;height:44px;background:var(--white);border-radius:7px;box-shadow:0 3px 0 #e2dfe4}
.pill{position:absolute;height:32px;border-radius:6px;font-size:11px;font-weight:600;line-height:32px;text-align:center}
.pill.dark{background:#16161b;color:var(--white)}
.pill.blue{background:var(--sky);color:var(--white)}
.pill.search{width:34px;background:var(--yellow)}
.pill.search::before{content:"";position:absolute;left:11px;top:10px;width:9px;height:9px;border:2px solid #1b1b1b;border-radius:50%}
.word-tile{position:absolute;width:116px;height:44px;background:var(--white);border-radius:8px;box-shadow:0 3px 0 #e3e1e6;font-family:"Fredoka",sans-serif;font-weight:500;font-size:20px;line-height:44px;text-align:center;color:#2a2a2a}
.cta{position:absolute;height:43px;border-radius:7px;background:var(--blue);color:var(--white);font-size:10px;font-weight:800;letter-spacing:.5px;line-height:43px;text-align:center;box-shadow:0 3px 0 #063a80}
.slot{position:absolute;width:35px;height:40px;border-radius:7px;background:#e9e9ee}
.letter{position:absolute;width:43px;height:44px;border-radius:8px;background:var(--white);box-shadow:0 3px 0 #e1e1e6;font-family:"Fredoka",sans-serif;font-weight:600;font-size:24px;line-height:42px;text-align:center}
.letter.used{background:#c9c9cf;color:#55555c}
/* sign up */
.signup{background:var(--navy);color:var(--white)}
.brand-word{position:absolute;left:0;width:100%;top:70px;text-align:center;font-family:"Fredoka",sans-serif;font-weight:600;font-size:26px;color:var(--yellow)}
.field{position:absolute;background:var(--white);border-radius:6px;box-shadow:0 3px 0 #9cb7e8}
.center-text{position:absolute;left:0;width:100%;text-align:center}
/* profile */
.card{position:absolute;background:var(--white);border-radius:8px;box-shadow:0 0 0 1px #eeeaf0}
.pfield{position:absolute;left:15px;width:208px;border:1px solid var(--line);border-radius:6px;background:var(--white);box-shadow:0 2px 0 #ececf1}
.pfield small{position:absolute;left:13px;top:6px;font-size:8px;color:var(--muted)}
.pfield span{position:absolute;left:13px;font-size:10px;font-weight:600;color:#2b2b33}
.pfield .arrow{position:absolute;right:12px;top:14px}
/* stats */
.tab{position:absolute;top:74px;height:28px;border-radius:5px;font-size:10px;font-weight:700;line-height:28px;text-align:center;border:1px solid var(--line);background:var(--white);color:#333}
.tab.active{background:var(--blue);color:var(--white);border-color:var(--blue)}
.chip{position:absolute;height:26px;padding:0 12px;border:1px solid var(--line);border-radius:5px;background:var(--white);font-size:10px;font-weight:600;line-height:24px;box-shadow:0 2px 0 #ececf1}
.axis{position:absolute;font-size:8px;color:var(--muted)}
</style>
</head>
<body>
<div class="board">
  <h1 class="board-title" style="top:92px;font-size:56px">ReadNest Learning App</h1>

  <div class="section-label" style="left:262px;top:252px">01.Main Screen</div>
  <div class="section-label" style="left:701px;top:252px">02.Main Screen one</div>
  <div class="section-label" style="left:1171px;top:252px">03.Main Screen two</div>
  <div class="section-label" style="left:262px;top:1063px">04.Main Screen three</div>
  <div class="section-label" style="left:692px;top:1063px">05.Profile</div>
  <div class="section-label" style="left:1178px;top:1063px">06.Stats</div>

  <!-- Sign up -->
  <section class="screen signup" style="left:256px;top:342px;height:613px">
    <div class="brand-word">ReadNest</div>
    <div class="center-text" style="top:123px;font-size:12px;font-weight:700">Learn letters and words</div>
    <div class="center-text" style="top:183px;font-family:'Fredoka',sans-serif;font-weight:500;font-size:15px">Create an account</div>
    <div class="center-text" style="top:208px;font-size:11px">Enter your email to sign up for this app</div>
    <div class="field" style="left:22px;top:240px;width:239px;height:40px">
      <span class="abs" style="left:16px;top:13px;width:13px;height:11px;border:1.5px solid #9b6ee8;border-radius:3px"></span>
      <span class="abs" style="left:41px;top:12px;font-size:10px;color:#a6a6b3">email@domain.com</span>
    </div>
    <div class="abs" style="left:22px;top:299px;width:239px;height:40px;border:2px solid #3a78d6;border-radius:6px;text-align:center;line-height:36px;font-size:10px;font-weight:800;letter-spacing:1.5px">SIGN UP WITH EMAIL</div>
    <div class="center-text" style="top:365px;font-size:10px;color:#c4d4f2">
      <span style="display:inline-block;width:36px;height:1px;background:#8aa6df;vertical-align:middle"></span>
      OR
      <span style="display:inline-block;width:36px;height:1px;background:#8aa6df;vertical-align:middle"></span>
    </div>
    <div class="field" style="left:22px;top:402px;width:239px;height:41px">
      <span class="abs" style="left:14px;top:13px;width:14px;height:14px;border-radius:50%;background:#4a86e8"></span>
      <span class="abs" style="left:40px;top:12px;font-size:11px;color:#3b3b46">Continue With Quorvix</span>
      <svg class="abs" style="left:213px;top:15px" width="12" height="10" viewBox="0 0 12 10"><path d="M0 5H11M7 1l4 4-4 4" stroke="#6b55e0" stroke-width="1.4" fill="none"/></svg>
    </div>
    <div class="center-text" style="top:460px;font-size:9.5px;line-height:20px;color:#d7e2f7">By clicking continue, you agree to our <b style="color:#fff">Terms of<br>Service</b> and <b style="color:#fff">Privacy Policy</b></div>
    <div class="abs" role="img" aria-label="Illustration of two children playing on grass with letter blocks" style="left:0;top:500px;width:284px;height:113px;background:linear-gradient(180deg,rgba(10,70,179,0) 0%,#5fbd3e 55%,#3f9a2b 100%)"></div>
  </section>

  <!-- Main screen one -->
  <section class="screen" style="left:701px;top:342px;height:613px">
    <div class="play-body"></div>
    <header class="app-header">
      <span class="menu-dot" style="left:8px"><i style="top:8px"></i><i style="top:11px"></i><i style="top:14px"></i></span>
      <span class="header-title" style="left:48px">Main Screen</span>
      <span class="points">16 Points</span>
      <svg width="284" height="12" viewBox="0 0 284 12"><path d="M0 0H284V2Q142 14 0 4Z" fill="#0a46b3"/></svg>
    </header>
    <div class="sound-btn" style="left:236px;top:73px"><svg width="14" height="14" viewBox="0 0 14 14"><path d="M1 5h3l4-4v12L4 9H1z" fill="#0a46b3"/><path d="M10 4q2 3 0 6" stroke="#0a46b3" stroke-width="1.5" fill="none"/></svg></div>
    <div class="art" role="img" aria-label="Illustration of a cartoon monkey sitting" style="left:79px;top:98px;width:130px;height:146px"></div>
    <div class="answer-box" style="left:49px;top:262px;width:186px"></div>
    <div class="pill dark" style="left:13px;top:343px;width:100px">Show All Words</div>
    <div class="pill blue" style="left:124px;top:343px;width:100px">Play All Words</div>
    <div class="pill search" style="left:235px;top:343px"></div>
    <div class="word-tile" style="left:16px;top:399px">onmkye</div>
    <div class="word-tile" style="left:152px;top:399px">monkey</div>
    <div class="word-tile" style="left:16px;top:454px">Keymon</div>
    <div class="word-tile" style="left:152px;top:454px">moyekn</div>
    <div class="cta" style="left:13px;top:529px;width:256px">SHOW ME THE RESULTS</div>
  </section>

  <!-- Main screen two -->
  <section class="screen" style="left:1181px;top:342px;height:613px">
    <div class="play-body"></div>
    <header class="app-header">
      <span class="menu-dot" style="left:8px"><i style="top:8px"></i><i style="top:11px"></i><i style="top:14px"></i></span>
      <span class="header-title" style="left:48px">Main Screen</span>
      <span class="points">16 Points</span>
      <svg width="284" height="12" viewBox="0 0 284 12"><path d="M0 0H284V2Q142 14 0 4Z" fill="#0a46b3"/></svg>
    </header>
    <div class="sound-btn" style="left:236px;top:73px"><svg width="14" height="14" viewBox="0 0 14 14"><path d="M1 5h3l4-4v12L4 9H1z" fill="#0a46b3"/><path d="M10 4q2 3 0 6" stroke="#0a46b3" stroke-width="1.5" fill="none"/></svg></div>
    <div class="answer-box" style="left:38px;top:262px;width:208px"></div>
    <div class="pill dark" style="left:13px;top:343px;width:100px">Show All Words</div>
    <div class="pill blue" style="left:124px;top:343px;width:100px">Play All Words</div>
    <div class="pill search" style="left:235px;top:343px"></div>
    <div class="word-tile" style="left:16px;top:399px">onmkye</div>
    <div class="word-tile" style="left:152px;top:399px">monkey</div>
    <div class="word-tile" style="left:16px;top:454px">Keymon</div>
    <div class="word-tile" style="left:152px;top:454px">moyekn</div>
    <div class="cta" style="left:13px;top:529px;width:256px">SHOW ME THE RESULTS</div>
  </section>

  <!-- Main screen three -->
  <section class="screen" style="left:272px;top:1166px;height:614px">
    <div class="play-body" style="background:var(--cream)"></div>
    <header class="app-header">
      <span class="menu-dot" style="left:9px"><i style="top:8px"></i><i style="top:11px"></i><i style="top:14px"></i></span>
      <span class="header-title" style="left:48px">Main Screen</span>
      <span class="points">16 Points</span>
      <svg width="284" height="12" viewBox="0 0 284 12"><path d="M0 0H284V2Q142 14 0 4Z" fill="#0a46b3"/></svg>
    </header>
    <div class="sound-btn" style="left:236px;top:73px"><svg width="14" height="14" viewBox="0 0 14 14"><path d="M1 5h3l4-4v12L4 9H1z" fill="#0a46b3"/><path d="M10 4q2 3 0 6" stroke="#0a46b3" stroke-width="1.5" fill="none"/></svg></div>
    <div class="art" role="img" aria-label="Illustration of a cartoon monkey sitting" style="left:83px;top:94px;width:126px;height:146px"></div>
    <div class="letter" style="left:15px;top:264px;width:34px;height:40px;line-height:38px;font-size:22px">m</div>
    <div class="slot" style="left:59px;top:264px"></div>
    <div class="slot" style="left:104px;top:264px"></div>
    <div class="slot" style="left:149px;top:264px"></div>
    <div class="slot" style="left:194px;top:264px"></div>
    <div class="slot" style="left:239px;top:264px"></div>
    <div class="pill dark" style="left:14px;top:342px;width:100px">Show All Words</div>
    <div class="pill blue" style="left:125px;top:342px;width:100px">Play All Words</div>
    <div class="pill search" style="left:236px;top:342px"></div>
    <div class="letter" style="left:17px;top:397px">o</div>
    <div class="letter" style="left:85px;top:397px">n</div>
    <div class="letter used" style="left:155px;top:397px">m</div>
    <div class="letter" style="left:223px;top:397px">k</div>
    <div class="letter" style="left:17px;top:461px">y</div>
    <div class="letter" style="left:85px;top:461px">e</div>
    <div class="cta" style="left:14px;top:529px;width:256px">SHOW ME THE RESULTS</div>
  </section>

  <!-- Profile -->
  <section class="screen" style="left:703px;top:1166px;height:679px">
    <header class="app-header">
      <span class="menu-dot" style="left:9px">
        <svg class="abs" style="left:8px;top:7px" width="8" height="10" viewBox="0 0 8 10"><path d="M6 1L2 5l4 4" stroke="#fff" stroke-width="1.6" fill="none"/></svg>
      </span>
      <span class="header-title" style="left:0;width:100%;text-align:center">Profile</span>
      <svg width="284" height="12" viewBox="0 0 284 12"><path d="M0 0H284V2Q142 14 0 4Z" fill="#0a46b3"/></svg>
    </header>
    <div class="card" style="left:22px;top:141px;width:240px;height:498px">
      <div class="pfield" style="top:70px;height:42px"><small>Name</small><span style="top:20px">Mara Quill</span>
        <svg class="arrow" width="11" height="9" viewBox="0 0 11 9"><path d="M0 4.5H10M6 1l4 3.5L6 8" stroke="#888" stroke-width="1.1" fill="none"/></svg></div>
      <div class="pfield" style="top:126px;height:42px"><small>Username</small><span style="top:20px">@username</span>
        <svg class="arrow" width="11" height="9" viewBox="0 0 11 9"><path d="M0 4.5H10M6 1l4 3.5L6 8" stroke="#888" stroke-width="1.1" fill="none"/></svg></div>
      <div class="pfield" style="top:181px;height:42px"><small>Email</small><span style="top:20px">name@domain.com</span>
        <svg class="arrow" width="11" height="9" viewBox="0 0 11 9"><path d="M0 4.5H10M6 1l4 3.5L6 8" stroke="#888" stroke-width="1.1" fill="none"/></svg></div>
      <div class="pfield" style="top:237px;height:66px"><small>Links</small>
        <b class="abs" style="right:8px;top:7px;padding:1px 6px;border-radius:3px;background:var(--yellow);font-size:7.5px;color:#6a4b00">Add Link</b>
        <span style="top:24px">website.net</span><span style="top:42px">mylink.net</span></div>
      <div class="pfield" style="top:316px;height:94px"><small>Bio</small>
        <span style="top:24px;right:10px;line-height:18px;font-weight:600">Lorem ipsum dolor sit amet, consectetur adipiscing elit, sed do eiusmod tempor incididunt.</span></div>
      <div class="cta" style="left:14px;top:433px;width:210px">LOGOUT</div>
    </div>
    <div class="abs" role="img" aria-label="Profile photo of a smiling girl" style="left:90px;top:82px;width:102px;height:102px;border-radius:50%;border:4px solid #fff;background:linear-gradient(160deg,#f27a92,#b83c5c);box-shadow:0 2px 6px rgba(0,0,0,.12)"></div>
    <span class="abs" style="left:178px;top:110px;width:20px;height:20px;border-radius:50%;background:var(--blue);border:2px solid #fff"></span>
  </section>

  <!-- Stats -->
  <section class="screen" style="left:1164px;top:1166px;height:654px">
    <header class="app-header">
      <span class="menu-dot" style="left:8px"><i style="top:8px"></i><i style="top:11px"></i><i style="top:14px"></i></span>
      <span class="header-title" style="left:0;width:100%;text-align:center">NestStats</span>
      <span class="abs" role="img" aria-label="User avatar photo" style="left:238px;top:14px;width:28px;height:28px;border-radius:50%;border:2px solid #fff;background:linear-gradient(160deg,#f27a92,#b83c5c)"></span>
      <svg width="284" height="12" viewBox="0 0 284 12"><path d="M0 0H284V2Q142 14 0 4Z" fill="#0a46b3"/></svg>
    </header>
    <div class="tab active" style="left:13px;width:76px">Ranking</div>
    <div class="tab" style="left:100px;width:102px">Correct Words</div>
    <div class="tab" style="left:214px;width:52px">Todo</div>
    <div class="abs" style="left:13px;top:131px;width:185px;height:63px;border-radius:6px;background:var(--peach);border:2px solid #fbd7b0">
      <span class="abs" role="img" aria-label="Third place trophy icon" style="left:10px;top:10px;width:40px;height:40px;border-radius:50%;background:#f59a2f"></span>
      <span class="abs" style="left:67px;top:12px;font-size:8px;color:#b69a80">Total Ranking</span>
      <span class="abs" style="left:67px;top:28px;font-family:'Fredoka',sans-serif;font-size:14px;color:#2a2a2a">3<sup style="font-size:7px">rd</sup> Place of 100</span>
    </div>
    <div class="abs" style="left:214px;top:131px;width:80px;height:63px;border-radius:6px;background:var(--white);border:1px solid var(--line)">
      <span class="abs" role="img" aria-label="Medal icon" style="left:11px;top:14px;width:26px;height:34px;border-radius:6px 6px 50% 50%;background:linear-gradient(#e84b4b 40%,#f5a623 40%)"></span>
    </div>
    <div class="card" style="left:14px;top:222px;width:252px;height:229px">
      <span class="abs" style="left:16px;top:12px;font-family:'Fredoka',sans-serif;font-size:14px">Learning curve</span>
      <span class="axis" style="left:16px;top:48px">100 Words day</span>
      <span class="axis" style="left:16px;top:80px">50 Words day</span>
      <svg class="abs" style="left:15px;top:52px" width="225" height="115" viewBox="0 0 225 115">
        <defs><linearGradient id="curveFill" x1="0" y1="0" x2="0" y2="1"><stop offset="0" stop-color="#5b9be8" stop-opacity=".7"/><stop offset="1" stop-color="#cfe2f8" stop-opacity=".15"/></linearGradient></defs>
        <line x1="0" y1="10" x2="222" y2="10" stroke="#e3e6ee"/>
        <line x1="0" y1="42" x2="222" y2="42" stroke="#e3e6ee"/>
        <path d="M0 108C15 92 28 78 42 86C55 94 62 112 72 104C85 92 88 55 100 40C112 26 125 14 137 18C152 24 158 62 175 56C192 50 205 22 219 8V115H0Z" fill="url(#curveFill)"/>
        <path d="M0 108C15 92 28 78 42 86C55 94 62 112 72 104C85 92 88 55 100 40C112 26 125 14 137 18C152 24 158 62 175 56C192 50 205 22 219 8" stroke="#2f72d6" stroke-width="2" fill="none"/>
        <circle cx="219" cy="8" r="4" fill="#2f72d6"/>
      </svg>
      <span class="axis" style="left:13px;top:193px">NOV 2</span>
      <span class="axis" style="left:58px;top:193px">3</span>
      <span class="axis" style="left:92px;top:193px">4</span>
      <span class="axis" style="left:125px;top:193px">5</span>
      <span class="axis" style="left:160px;top:193px">6</span>
      <span class="axis" style="left:194px;top:193px">7</span>
      <span class="axis" style="left:228px;top:193px">8</span>
    </div>
    <div class="card" style="left:14px;top:476px;width:252px;height:135px">
      <span class="abs" style="left:16px;top:14px;font-family:'Fredoka',sans-serif;font-size:14px">Recently learned words</span>
      <span class="chip" style="left:16px;top:48px">Monkey</span>
      <span class="chip" style="left:91px;top:48px">Correct</span>
      <span class="chip" style="left:167px;top:48px">Banana</span>
      <span class="chip" style="left:16px;top:89px">Drawing</span>
      <span class="chip" style="left:93px;top:89px">Peacock</span>
    </div>
  </section>

  <h2 class="board-title" style="top:1975px;font-size:58px">Thanks for Watching My work</h2>
</div>
</body>
</html>
```